Bold Cover needed for a book on Workplace Bullying

I need a book cover design for a book titled, “Iron Silence?” The book recounts my story of bullying in the workplace. It also includes chapters on how readers can minimize/stop workplace bullying, write an effective complaint, and ensure their own mental wellbeing.
I am looking for a bold design using red and black, and possibly distressed lettering. The covers of other books dealing with this subject do not reflect my vision. They are often too childish or look too academic. This book needs to stress the serious nature of a toxic workplace, while appealing to readers experiencing a similar situation. I’d like the cover to reflect the mental anguish associated with workplace bullying (hence the distressed lettering).
I have included a cover that appeals to me (although the coloring is wrong). That said, I am also very happy (and excited) to see your creative input!
On the cover, it should have the following:
Title: Iron Silence?
Subtitle: How the Harbour Works Department Condones Bullying & Ruins Lives
Author: Owen Frick
Other relevant details:
Book size: 5.5” x 8.5”
Back cover will have a blurb, author picture/short bio, and barcode
The blurb on the back cover reads:
Undermining, intimidation and threats
Despite the Department of Harbour Works allegedly holding a zero tolerance for bullying, these behaviours were an everyday occurrence in at least one workplace. Even after a decade of complaints, numerous witnesses and physical proof, the department failed to act. Instead, they looked the other way, allowing one powerful and well-connected individual to end careers and ruin lives.
After being targeted, one teacher resolved to put an end to the abuse experienced by more than fifty employees. His startling story reveals the relentless bullying, mental health ramifications, and insidious tactics used to cover up the corrosive behaviour.
Those who have experienced a toxic workplace will also find much needed support and guidance, intended to minimise suffering and detail a clear way forward. Chapters include dealing with bullying in the workplace, how to lodge a successful complaint, and how to stay sane during any potential legal action.

```html
<!DOCTYPE html>
<html lang="en">
<head>
<meta charset="utf-8">
<title>Iron Silence? — Book Cover</title>
<link rel="stylesheet" href="https://fonts.googleapis.com/css2?family=Anton&display=swap">
<style>
  :root {
    --backdrop: #a81116;
    --title-red: #c0141b;
    --shadow-ink: #1e0607;
    --night: #26282d;
    --storm: #484c54;
    --cloud-dark: #1f2125;
    --glow: #eef1f3;
    --band-dark: #240306;
    --band-mid: #4e080d;
    --band-red: #8a1218;
    --mist: #b4c0cb;
    --ink: #111111;
  }
  * { margin: 0; padding: 0; box-sizing: border-box; }
  html, body {
    width: 1200px;
    height: 800px;
    overflow: hidden;
    background: var(--backdrop);
  }
  .canvas {
    position: relative;
    width: 1200px;
    height: 800px;
  }
  .book-cover {
    position: absolute;
    left: 408px;
    top: 94px;
    width: 397px;
    height: 606px;
    overflow: hidden;
    border-radius: 3px;
    background: var(--night);
  }
  .cover-art {
    position: absolute;
    inset: 0;
    background:
      radial-gradient(ellipse 150px 220px at 100% 56%, var(--cloud-dark) 0%, rgba(31,33,37,0.9) 55%, rgba(31,33,37,0) 100%),
      radial-gradient(ellipse 190px 170px at 40% 82%, var(--glow) 0%, #d9dfe3 40%, rgba(110,118,126,0.55) 75%, rgba(38,40,45,0) 100%),
      linear-gradient(180deg, var(--night) 0%, var(--storm) 50%, #3a3d44 100%);
  }
  .ground-bands {
    position: absolute;
    left: 0;
    bottom: 0;
    width: 397px;
    height: 115px;
  }
  .cover-title {
    position: absolute;
    left: 38px;
    top: 12px;
    font-family: "Anton", "Impact", sans-serif;
    font-weight: 400;
    font-size: 76px;
    line-height: 1;
    color: var(--title-red);
    text-transform: uppercase;
    text-shadow: 2px 2px 0 var(--shadow-ink);
  }
  .cover-subtitle {
    position: absolute;
    left: 38px;
    top: 171px;
    font-family: "Anton", "Impact", sans-serif;
    font-weight: 400;
    font-size: 44px;
    line-height: 49px;
    color: var(--title-red);
    text-transform: uppercase;
    text-shadow: 2px 2px 0 var(--shadow-ink);
  }
  .cover-author {
    position: absolute;
    right: 36px;
    bottom: 14px;
    font-family: "Anton", "Impact", sans-serif;
    font-weight: 400;
    font-size: 21px;
    line-height: 1;
    color: var(--ink);
    text-transform: uppercase;
  }
</style>
</head>
<body>
  <main class="canvas">
    <section class="book-cover">
      <div class="cover-art" role="img" aria-label="Illustration: a lone man in a dark suit and red tie stands on a ridge in a bright central glow, with dark storm clouds and shadowy machinery closing in around him"></div>

      <svg class="ground-bands" viewBox="0 0 397 115" aria-hidden="true">
        <path d="M0 16 Q200 -4 397 14 L397 115 L0 115 Z" fill="var(--band-dark)"/>
        <path d="M0 34 Q200 16 397 30 L397 115 L0 115 Z" fill="var(--band-mid)"/>
        <path d="M0 52 Q200 34 397 46 L397 115 L0 115 Z" fill="var(--band-red)"/>
        <path d="M0 112 Q200 62 397 52 L397 115 L0 115 Z" fill="var(--mist)"/>
      </svg>

      <h1 class="cover-title">Iron<br>Silence?</h1>
      <p class="cover-subtitle">How the Harbour<br>Works Department<br>Condones Bullying<br>&amp; Ruins Lives</p>
      <p class="cover-author">Owen Frick</p>
    </section>
  </main>
</body>
</html>
```